Volt9ine Electrical Services Needs A Flyer Design

We need a flyer design for a new business based in Sydney, Australia called Volt9ine Electrical Services. We provide services for residential,commercial and industrial works. Services include Electrical Design, Installation, Repairs & Maintenance. Communications Installation, Cabling, Maintenance & Repairs. Over 25 years Industry Experience.Service Calls, Quick Response Time, Professional Service. We would like to see designs that use the colors red,white and blue similar to the logo. The final Design should be creative as the business logo suggests and should communicate the businesses services.

Target Market(s)

Residential

Industry/Entity Type

Industrial

Font styles to use
Sans Serif

Requirements
Must have
• My project must have the logo provided utilized in the flyer.It must list the following contact name and number Sam 0471 392 618 services as above in the project description. Flyer should be DL size (99mmx210mm).

```html
<!DOCTYPE html>
<html lang="en">
<head>
<meta charset="utf-8">
<title>Volt9ine Electrical Services – Flyer</title>
<link rel="stylesheet" href="https://fonts.googleapis.com/css2?family=Roboto:wght@700;900&family=Lato:ital,wght@1,700&family=Montserrat:wght@600;700&display=swap">
<style>
  :root {
    --navy: #1c3a8c;
    --navy-deep: #12276a;
    --red: #d01f27;
    --white: #ffffff;
    --paper: #f4f5f7;
    --ink: #1d1d24;
    --stage: #e6e4e0;
  }
  * { margin: 0; padding: 0; box-sizing: border-box; }
  html, body { width: 902px; height: 1200px; overflow: hidden; }
  body { background: var(--stage); position: relative; }

  .flyer {
    position: absolute; left: 181px; top: 30px;
    width: 540px; height: 1140px;
    background: linear-gradient(180deg, var(--white), var(--paper));
    overflow: hidden;
    box-shadow: 0 6px 22px rgba(0,0,0,.18);
  }
  .flyer-shapes { position: absolute; inset: 0; }

  .brand { position: absolute; top: 44px; left: 0; width: 100%; text-align: center; color: var(--white); font-family: "Montserrat", sans-serif; font-weight: 700; }
  .brand-name { font-size: 50px; letter-spacing: 4px; line-height: 1; text-transform: uppercase; }
  .brand-sub { font-size: 16px; letter-spacing: 3px; margin-top: 12px; text-transform: uppercase; }

  .headline { position: absolute; left: 0; width: 100%; text-align: center; font-family: "Roboto", sans-serif; font-weight: 900; line-height: 1; }
  .headline-years { top: 213px; font-size: 57px; color: var(--red); }
  .headline-experience { top: 285px; font-size: 37px; color: var(--navy); font-weight: 700; }

  .services-tab {
    position: absolute; left: 0; top: 352px; width: 310px; height: 38px;
    background: var(--navy); border-radius: 0 19px 19px 0;
    color: var(--white); font-family: "Montserrat", sans-serif; font-weight: 600;
    font-size: 21px; letter-spacing: 3px; line-height: 38px; padding-left: 22px;
    font-variant: small-caps;
  }
  .services-list { position: absolute; left: 22px; top: 404px; list-style: none; }
  .services-list li {
    font-family: "Lato", sans-serif; font-style: italic; font-weight: 700;
    font-size: 22px; color: var(--ink); height: 41px; line-height: 34px;
    display: flex; align-items: center; gap: 10px;
  }
  .services-list li::before {
    content: ""; width: 9px; height: 9px; border-radius: 50%;
    border: 2px solid var(--red); background: var(--navy); flex: none;
  }

  .electrician-photo {
    position: absolute; left: 346px; top: 356px; width: 168px; height: 520px;
    border-radius: 70px 70px 10px 10px;
    background: linear-gradient(180deg, #e88a3a 0%, #2a3c7a 18%, #22336a 60%, #1c2a55 100%);
    opacity: .85;
  }
  .plug-cable-art {
    position: absolute; left: 110px; top: 780px; width: 80px; height: 110px;
    border-radius: 8px;
    background: linear-gradient(180deg, #e0474d, var(--red));
    opacity: .85;
  }

  .booking { position: absolute; left: 0; width: 100%; text-align: center; color: var(--white); font-family: "Montserrat", sans-serif; font-weight: 600; font-variant: small-caps; letter-spacing: 3px; }
  .booking-line { font-size: 22px; }
  .booking-1 { top: 962px; }
  .booking-2 { top: 996px; }
  .booking-call { top: 1035px; font-size: 26px; font-weight: 700; }
  .contact { position: absolute; top: 1080px; left: 0; width: 100%; text-align: center; font-family: "Roboto", sans-serif; font-weight: 700; color: var(--white); font-size: 34px; line-height: 1; }
  .contact-name { display: inline-block; background: var(--red); font-size: 26px; padding: 2px 6px; margin-right: 6px; vertical-align: 3px; }
</style>
</head>
<body>
  <main class="flyer">
    <svg class="flyer-shapes" width="540" height="1140" viewBox="0 0 540 1140" aria-hidden="true">
      <defs>
        <linearGradient id="navyGrad" x1="0" y1="0" x2="0" y2="1">
          <stop offset="0" stop-color="#2546a8"/>
          <stop offset="1" stop-color="#12276a"/>
        </linearGradient>
      </defs>
      <path d="M0 0 H540 V205 Q270 150 0 205 Z" fill="url(#navyGrad)"/>
      <path d="M0 205 Q270 150 540 205" fill="none" stroke="#d01f27" stroke-width="5"/>
      <path d="M0 215 Q270 160 540 215 V225 Q270 172 0 225 Z" fill="#ffffff"/>
      <path d="M6 1140 Q270 660 534 1140 Z" fill="#d01f27"/>
      <path d="M16 1140 Q270 676 524 1140 Z" fill="#ffffff"/>
      <path d="M26 1140 Q270 694 514 1140 Z" fill="url(#navyGrad)"/>
    </svg>

    <header class="brand">
      <div class="brand-name">Volt9ine</div>
      <div class="brand-sub">Electrical Services</div>
    </header>

    <h1 class="headline headline-years">OVER 25 YEARS</h1>
    <h2 class="headline headline-experience">INDUSTRY EXPERIENCE</h2>

    <div class="services-tab">Our Services</div>
    <ul class="services-list">
      <li>Electrical Design</li>
      <li>Installation</li>
      <li>Repairs &amp; Maintenance</li>
      <li>Communications Installation</li>
      <li>Cabling</li>
      <li>Maintenance &amp; Repairs</li>
      <li>Service Calls</li>
      <li>Quick Response Time</li>
      <li>Professional Service</li>
    </ul>

    <div class="plug-cable-art" role="img" aria-label="Red power plug illustration with its cable curving down to the bottom of the flyer"></div>
    <div class="electrician-photo" role="img" aria-label="Photo of an electrician in hard hat and navy workwear holding a multimeter, with cable coiled over his shoulder"></div>

    <p class="booking booking-line booking-1">For booking</p>
    <p class="booking booking-line booking-2">an appointment</p>
    <p class="booking booking-call">Call Us today</p>
    <p class="contact"><span class="contact-name">Sam</span>0471 392 618</p>
  </main>
</body>
</html>
```